Custom Home Builder Website

We need a re-design of a website for our client: "http://www.tovarelbuilds.com". Their current design is outdated and has flash. We need to make it responsive for all devices and with a more professional look.

Pages to consider:
1. Home page
2. Portfolio page - gallery of projects (multiple images of a project with captions, and a main text area for each project).

Good clean design reflecting quality craftsmanship is a must.

We only need designs, no coding required

Target Market(s)

The intended market is home owners looking to build with a reputable and professional home builder.

Industry/Entity Type

Home Builder

Requirements
Must have
• Must Have:
• - main areas of site: home, portfolio, video gallery, contact
Nice to have
• - Maybe pullquotes from testimonials placed as slideshow?

```html
<!DOCTYPE html>
<html lang="en">
<head>
<meta charset="utf-8">
<title>Tovarel Built — Portfolio</title>
<link rel="stylesheet" href="https://fonts.googleapis.com/css2?family=Arimo:wght@400;700&family=Open+Sans:wght@400;600&display=swap">
<style>
  :root {
    --ink: #2b2b2b;
    --bar: #323230;
    --gold: #b58f5f;
    --rust: #a8622a;
    --text-grey: #8d8d8d;
    --footer: #30302e;
    --footer-base: #262624;
    --footer-link: #b7b7b5;
    --beige: #e8dcc6;
    --white: #ffffff;
  }
  * { margin: 0; padding: 0; box-sizing: border-box; }
  html, body { width: 1085px; height: 1200px; overflow: hidden; background: var(--white); }
  body { position: relative; font-family: "Open Sans", Arial, sans-serif; color: var(--ink); }
  .abs { position: absolute; }

  /* Hero */
  .hero {
    left: 0; top: 0; width: 1085px; height: 524px;
    background:
      radial-gradient(ellipse at 30% 35%, #b9a276 0%, rgba(185,162,118,0) 45%),
      radial-gradient(ellipse at 55% 70%, #6a3a1e 0%, rgba(106,58,30,0) 50%),
      linear-gradient(90deg, #5a4a3a 0%, #8a7256 20%, #a48a66 40%, #7a5c44 65%, #8f8a84 85%, #6f6c68 100%);
  }
  .hero-line { left: 0; top: 0; width: 1085px; height: 2px; background: #7a5a32; }
  .call { right: 184px; top: 13px; color: var(--white); font-family: Arimo, Arial, sans-serif; font-size: 11px; font-weight: 700; letter-spacing: .2px; }
  .call span { font-size: 15px; font-weight: 400; }

  .brand { left: 166px; top: 38px; width: 190px; height: 58px; }
  .brand-name { left: 186px; top: 52px; font-family: "Open Sans", Arial, sans-serif; font-size: 22px; font-weight: 600; color: var(--gold); letter-spacing: 1px; }
  .nav { left: 332px; top: 38px; width: 585px; height: 58px; }
  .nav-list { left: 359px; top: 38px; height: 58px; display: flex; list-style: none; font-family: Arimo, Arial, sans-serif; font-size: 12px; color: var(--white); }
  .nav-list li { line-height: 58px; }

  .slide-arrow { top: 262px; }
  .headline { left: 181px; top: 426px; font-size: 38px; color: var(--white); letter-spacing: .3px; font-weight: 400; }
  .learn { left: 738px; top: 439px; width: 160px; height: 31px; }
  .learn-label { left: 763px; top: 448px; font-family: Arimo, Arial, sans-serif; font-size: 11px; color: var(--white); letter-spacing: .4px; }

  /* Content */
  .panel { left: 167px; top: 498px; width: 751px; height: 520px;
    background: linear-gradient(180deg, var(--beige) 0%, #f6f1e8 35px, var(--white) 75px);
    box-shadow: 0 0 10px rgba(0,0,0,.06); }
  .panel-wing { top: 498px; }
  .section-title { left: 184px; top: 530px; font-size: 14px; font-weight: 400; letter-spacing: .5px; color: var(--ink); }

  .card { width: 198px; }
  .card-title { font-size: 11.5px; color: var(--rust); letter-spacing: .2px; font-weight: 400; margin-bottom: 3px; line-height: 14px; }
  .card-photo { width: 198px; height: 100px; border: 1px solid #4b4b4b; }
  .card-text { margin-top: 8px; font-family: Arimo, Arial, sans-serif; font-size: 9.6px; line-height: 14px; color: var(--text-grey); letter-spacing: .35px; }
  .card-more { margin-top: 2px; display: block; font-family: Arimo, Arial, sans-serif; font-size: 10px; color: var(--rust); text-decoration: none; letter-spacing: .3px; }
  .divider { width: 1px; background: linear-gradient(180deg, rgba(0,0,0,0), #ececec 20%, #ececec 80%, rgba(0,0,0,0)); }

  .photo-homes { background: linear-gradient(180deg, #8a96a0 0%, #5f6a70 50%, #4b4d48 100%); }
  .photo-remodel { background: linear-gradient(180deg, #b8c4c8 0%, #c98a3c 45%, #6d5d4e 100%); }
  .photo-kitchen { background: linear-gradient(90deg, #d6d2c8 0%, #8c6a4c 50%, #4d3426 100%); }
  .photo-equestrian { background: linear-gradient(180deg, #9e9a92 0%, #8a7a66 55%, #c57a3a 100%); }
  .photo-projects { background: linear-gradient(180deg, #b8c6d2 0%, #8e8460 45%, #5b7a3c 100%); }

  /* Footer */
  .footer { left: 0; top: 1018px; width: 1085px; height: 137px; background: var(--footer); border-top: 4px solid #d9cfbf; }
  .footer-base { left: 0; top: 1155px; width: 1085px; height: 45px; background: var(--footer-base); }
  .copyright { left: 0; top: 1171px; width: 1085px; text-align: center; font-family: Arimo, Arial, sans-serif; font-size: 10px; color: #a9a9a7; letter-spacing: .3px; }
  .copyright span { color: var(--gold); }
  .footer-col h3 { font-size: 14px; font-weight: 400; color: var(--gold); letter-spacing: .3px; margin-bottom: 11px; }
  .footer-col ul { list-style: none; font-family: Arimo, Arial, sans-serif; font-size: 9.6px; color: var(--footer-link); letter-spacing: .3px; }
  .footer-col li { line-height: 16.5px; }
  .footer-col li.active { color: var(--gold); }
  .contact-list li { display: flex; align-items: flex-start; gap: 6px; line-height: 11px; margin-bottom: 9px; }
  .contact-list svg { flex: none; margin-top: 1px; }
</style>
</head>
<body>

<!-- Hero -->
<div class="abs hero" role="img" aria-label="Dining room with round wooden table, chairs and tall windows overlooking autumn trees"></div>
<div class="abs hero-line"></div>
<div class="abs call">CALL US ON : <span>(503) 555-0148</span></div>

<svg class="abs brand" width="190" height="58" viewBox="0 0 190 58"><polygon points="0,0 166,0 190,58 0,58" fill="#ffffff"/></svg>
<div class="abs brand-name">Tovarel Built</div>

<svg class="abs nav" width="585" height="58" viewBox="0 0 585 58">
  <polygon points="0,0 585,0 585,58 24,58" fill="#323230"/>
  <polygon points="195,0 267,0 290,58 218,58" fill="#b58f5f"/>
</svg>
<ul class="abs nav-list">
  <li style="margin-right:34px">Home</li>
  <li style="margin-right:19px">About Us</li>
  <li style="margin-right:20px">Services</li>
  <li style="margin-right:22px">Portfolio</li>
  <li style="margin-right:21px">Video Gallery</li>
  <li style="margin-right:21px">Tovarel Rewards</li>
  <li style="margin-right:22px">News</li>
  <li>Contact</li>
</ul>

<svg class="abs slide-arrow" style="left:142px" width="28" height="48" viewBox="0 0 28 48"><polyline points="25,2 3,24 25,46" fill="none" stroke="#ffffff" stroke-width="1.5"/></svg>
<svg class="abs slide-arrow" style="left:916px" width="28" height="48" viewBox="0 0 28 48"><polyline points="3,2 25,24 3,46" fill="none" stroke="#2b2b2b" stroke-width="1.5"/></svg>

<h1 class="abs headline">When You Want it Done Right</h1>
<svg class="abs learn" width="160" height="31" viewBox="0 0 160 31">
  <rect x="0.5" y="0.5" width="159" height="30" fill="#2e2e2c" stroke="#b58f5f"/>
  <polygon points="112,1 159.5,1 159.5,30.5 122,30.5" fill="#b58f5f"/>
  <polyline points="138,9 144,15.5 138,22" fill="none" stroke="#2b2b2b" stroke-width="1.3"/>
</svg>
<div class="abs learn-label">LEARN MORE</div>

<!-- Portfolio panel -->
<svg class="abs panel-wing" style="left:148px" width="20" height="26" viewBox="0 0 20 26"><polygon points="20,0 20,26 0,26" fill="#e6dac4"/></svg>
<svg class="abs panel-wing" style="left:917px" width="20" height="26" viewBox="0 0 20 26"><polygon points="0,0 20,26 0,26" fill="#e6dac4"/></svg>
<div class="abs panel"></div>
<h2 class="abs section-title">PORTFOLIO</h2>

<div class="abs divider" style="left:410px; top:560px; height:200px"></div>
<div class="abs divider" style="left:673px; top:560px; height:200px"></div>
<div class="abs divider" style="left:543px; top:790px; height:200px"></div>

<article class="abs card" style="left:181px; top:560px">
  <h3 class="card-title">Custom Homes</h3>
  <div class="card-photo photo-homes" role="img" aria-label="Modern single-storey custom home under a cloudy sky"></div>
  <p class="card-text">Lorem ipsum dolor sit amet, consectetur adipiscing elit. Proin sit amet dui velit. Class aptent taciti sociosqu ad litora torquent per per inceptos himenaeos.</p>
  <a class="card-more" href="#">READ MORE &gt;&gt;</a>
</article>

<article class="abs card" style="left:444px; top:560px">
  <h3 class="card-title">Remodels/ Additions</h3>
  <div class="card-photo photo-remodel" role="img" aria-label="Wooden deck with patio furniture overlooking autumn forest"></div>
  <p class="card-text">Lorem ipsum dolor sit amet, consectetur adipiscing elit. Proin sit amet dui velit. Class aptent taciti sociosqu ad litora torquent per per inceptos himenaeos.</p>
  <a class="card-more" href="#">READ MORE &gt;&gt;</a>
</article>

<article class="abs card" style="left:705px; top:560px">
  <h3 class="card-title">Kitchens/ Bathrooms</h3>
  <div class="card-photo photo-kitchen" role="img" aria-label="Bathroom with soaking tub, wood cabinetry and large windows"></div>
  <p class="card-text">Lorem ipsum dolor sit amet, consectetur adipiscing elit. Proin sit amet dui velit. Class aptent taciti sociosqu ad litora torquent per per inceptos himenaeos.</p>
  <a class="card-more" href="#">READ MORE &gt;&gt;</a>
</article>

<article class="abs card" style="left:314px; top:790px">
  <h3 class="card-title">Equestrian</h3>
  <div class="card-photo photo-equestrian" role="img" aria-label="Interior hallway with wooden staircase and hardwood floor"></div>
  <p class="card-text">Lorem ipsum dolor sit amet, consectetur adipiscing elit. Proin sit amet dui velit. Class aptent taciti sociosqu ad litora torquent per per inceptos himenaeos.</p>
  <a class="card-more" href="#">READ MORE &gt;&gt;</a>
</article>

<article class="abs card" style="left:575px; top:790px">
  <h3 class="card-title">Current Projects</h3>
  <div class="card-photo photo-projects" role="img" aria-label="Paved driveway with brick gate posts through green pasture"></div>
  <p class="card-text">Lorem ipsum dolor sit amet, consectetur adipiscing elit. Proin sit amet dui velit. Class aptent taciti sociosqu ad litora torquent per per inceptos himenaeos.</p>
  <a class="card-more" href="#">READ MORE &gt;&gt;</a>
</article>

<!-- Footer -->
<footer class="abs footer"></footer>

<div class="abs footer-col" style="left:183px; top:1040px">
  <h3>SUPPORTS</h3>
  <ul><li>Portfolio</li><li class="active">Tovarel Rewards</li><li>News</li></ul>
</div>
<div class="abs footer-col" style="left:381px; top:1040px">
  <h3>LEGAL INFO</h3>
  <ul><li>Terms Of Use</li><li>Privacy Policy</li><li>Copyright Policy</li></ul>
</div>
<div class="abs footer-col" style="left:566px; top:1040px">
  <h3>MORE</h3>
  <ul><li>Get Start</li><li>Learn More</li><li>Log In</li></ul>
</div>
<div class="abs footer-col" style="left:730px; top:1040px">
  <h3>CONTACT US</h3>
  <ul class="contact-list">
    <li>
      <svg width="10" height="9" viewBox="0 0 10 9"><polygon points="5,0 10,4.5 8.5,4.5 8.5,9 1.5,9 1.5,4.5 0,4.5" fill="#b58f5f"/></svg>
      <span>4180 NW Alder Ridge Rd, #210, Fairmont,<br>OR 97000</span>
    </li>
    <li>
      <svg width="10" height="10" viewBox="0 0 10 10"><rect width="10" height="10" rx="1.5" fill="#b58f5f"/><path d="M3 2.5c0 3 1.5 5 4.5 5.5l.5-1.3-1.4-.6-.6.6C5 6.2 4.3 5.4 3.9 4.4l.6-.6-.6-1.4z" fill="#30302e"/></svg>
      <span>(503) 555-0148</span>
    </li>
    <li>
      <svg width="10" height="8" viewBox="0 0 10 8"><rect width="10" height="8" fill="#b58f5f"/><polyline points="0,0 5,4.5 10,0" fill="none" stroke="#30302e" stroke-width="1"/></svg>
      <span>info@tovarelbuilds.com</span>
    </li>
  </ul>
</div>

<div class="abs footer-base"></div>
<p class="abs copyright">© 2010 <span>Tovarel</span> Custom Homes</p>

</body>
</html>
```